Business Cards for an 'affordable luxury' inner city home builder in Calgary.

We need a business card design that emulates the progressive, innovative, culture of our company and the modern style of our homes. Use our website www.velmarcrest-ab.com as a reference for the product we build.

Our company builds homes in the inner city space of Calgary, Alberta. We build affordable luxury.

Target Market(s)

Young professional Families

Contact Information for Business Card

Try to maintain consistency with the logo font and the card font.

Requirements
Must have
• The details must include: Name, education, title, phone number, website and email (Address is not as important)
• The design must be uniques (like our logo), elegant, sophisticated and modern.

```html
<!DOCTYPE html>
<html lang="en">
<head>
<meta charset="utf-8">
<title>Velmarcrest Custom Homes – Business Cards</title>
<link rel="stylesheet" href="https://fonts.googleapis.com/css2?family=Montserrat:wght@400;500;600&display=swap">
<style>
  :root {
    --backdrop: #333333;
    --card-light: #ececec;
    --card-dark: #1e1e1e;
    --ink: #1d1d1d;
    --ink-soft: #777777;
    --paper-text: #e9e9e9;
    --mark-grey: #8a8a8a;
  }
  * { margin: 0; padding: 0; box-sizing: border-box; }
  html, body {
    width: 1200px; height: 1200px; overflow: hidden;
    background: var(--backdrop);
    font-family: "Montserrat", Arial, sans-serif;
  }
  .card {
    position: absolute; left: 228px; width: 744px; height: 424px;
  }
  .card--front { top: 136px; background: var(--card-light); color: var(--ink); }
  .card--back { top: 640px; background: var(--card-dark); color: var(--paper-text); }

  .brand { position: absolute; display: flex; align-items: center; gap: 26px; }
  .brand__square { width: 72px; height: 72px; background: var(--mark-grey); flex: none; }
  .brand__name {
    font-weight: 500; font-size: 33px; line-height: 35px;
    letter-spacing: 0.5px; text-transform: uppercase;
  }
  .card--front .brand { left: 52px; top: 52px; }
  .card--back .brand { left: 150px; top: 160px; }

  .holder { position: absolute; left: 52px; top: 218px; }
  .holder__name { font-size: 21px; font-weight: 400; letter-spacing: 0.4px; text-transform: uppercase; }
  .holder__name strong { font-weight: 600; }
  .holder__credential { font-size: 16px; color: var(--ink-soft); line-height: 24px; }
  .holder__credential:first-of-type { margin-top: 4px; }

  .rule { position: absolute; left: 52px; top: 305px; width: 44px; height: 2px; background: var(--ink); }

  .contact { position: absolute; left: 52px; top: 331px; font-size: 16px; line-height: 24px; color: var(--ink-soft); }
  .contact__sep { color: var(--ink); font-weight: 600; }
  .contact strong { color: var(--ink); font-weight: 600; }
</style>
</head>
<body>
  <section class="card card--front">
    <div class="brand">
      <span class="brand__square"></span>
      <p class="brand__name">Velmarcrest<br>Custom<br>Homes Ltd</p>
    </div>
    <div class="holder">
      <p class="holder__name"><strong>Rajvinder -</strong> Co-Founder</p>
      <p class="holder__credential">Professional Engineer (P.ENG)</p>
      <p class="holder__credential">Masters of Business Administration (MBA)</p>
    </div>
    <div class="rule"></div>
    <div class="contact">
      <p>403-555-0148 <span class="contact__sep">/</span> projects@velmarcrest-ab.com</p>
      <p>www.<strong>velmarcrest-ab</strong>.com</p>
    </div>
  </section>

  <section class="card card--back">
    <div class="brand">
      <span class="brand__square"></span>
      <p class="brand__name">Velmarcrest<br>Custom<br>Homes Ltd</p>
    </div>
  </section>
</body>
</html>
```